Dribblecake Bites
2 x business cards, letter head, with complements and envelopes
Dribblecake Bites - Food
Creative Brief
Bright & Fun-filled
Percy Lantern
Managing Director
NA
Percy.Lantern@dribblecakebites.com.au
www.dribblecakebites.com.au
card 2 Teodor Blum Business Manager 0417583926 Teodorblum@quillnet.com www.dribblecakebites.com.au
logo ect

```html
<!DOCTYPE html>
<html lang="en">
<head>
<meta charset="utf-8">
<title>Dribblecake Bites – Business Card</title>
<link rel="stylesheet" href="https://fonts.googleapis.com/css2?family=PT+Sans:wght@400;700&family=Tinos&display=swap">
<style>
  :root {
    --backdrop: #3a3a3a;
    --card: #ffffff;
    --cocoa: #5a1e0e;
    --caramel: #c8611c;
    --tab-dark: #4a180b;
    --tab-light: #8a3a1c;
    --ink: #3b2a22;
    --rule: #cfc6c0;
  }
  * { box-sizing: border-box; margin: 0; padding: 0; }
  html, body {
    width: 1200px;
    height: 780px;
    overflow: hidden;
    background: var(--backdrop);
  }
  .card {
    position: absolute;
    left: 150px;
    top: 130px;
    width: 900px;
    height: 520px;
    background: var(--card);
    border-radius: 34px;
    box-shadow: 0 10px 30px rgba(0,0,0,0.45);
  }
  .edge-tab {
    position: absolute;
    top: 330px;
    width: 16px;
    height: 96px;
    background: linear-gradient(90deg, var(--tab-dark), var(--tab-light));
  }
  .edge-tab--left { left: 0; border-radius: 0 6px 6px 0; }
  .edge-tab--right { right: 0; border-radius: 6px 0 0 6px; background: linear-gradient(90deg, var(--tab-light), var(--tab-dark)); }

  .brand {
    position: absolute;
    left: 62px;
    top: 160px;
    display: flex;
    align-items: center;
    gap: 14px;
  }
  .brand-dot {
    width: 36px;
    height: 36px;
    border-radius: 50%;
    background: var(--caramel);
  }
  .brand-name {
    font-family: "PT Sans", sans-serif;
    font-weight: 700;
    font-size: 72px;
    line-height: 1;
    color: var(--cocoa);
    letter-spacing: -1px;
  }

  .person {
    position: absolute;
    right: 580px;
    top: 325px;
    text-align right;
    text-align: right;
    font-family: "PT Sans", sans-serif;
  }
  .person-name {
    font-weight: 700;
    font-size: 34px;
    color: var(--cocoa);
    line-height: 1.15;
  }
  .person-title {
    font-weight: 700;
    font-size: 26px;
    color: var(--caramel);
  }
  .divider {
    position: absolute;
    left: 340px;
    top: 305px;
    width: 2px;
    height: 120px;
    background: var(--rule);
  }
  .contacts {
    position: absolute;
    left: 358px;
    top: 305px;
    list-style: none;
    font-family: "Tinos", serif;
    font-size: 23px;
    color: var(--ink);
  }
  .contacts li {
    display: flex;
    align-items: center;
    gap: 12px;
    height: 40px;
  }
  .contacts svg { width: 20px; height: 20px; flex: none; }
</style>
</head>
<body>
  <main class="card">
    <div class="edge-tab edge-tab--left"></div>
    <div class="edge-tab edge-tab--right"></div>

    <div class="brand">
      <span class="brand-dot"></span>
      <span class="brand-name">Dribblecake Bites</span>
    </div>

    <div class="person">
      <p class="person-name">Percy Lantern</p>
      <p class="person-title">Managing Director</p>
    </div>
    <div class="divider"></div>

    <ul class="contacts">
      <li>
        <svg viewBox="0 0 20 20" aria-hidden="true"><path d="M5 2 C3 3 2 5 3 8 C5 13 8 16 12 17 C15 18 17 17 18 15 L15 12 L12.5 13.5 C10 12.5 7.5 10 6.5 7.5 L8 5 Z" fill="var(--cocoa)"/></svg>
        <span>0438160275</span>
      </li>
      <li>
        <svg viewBox="0 0 20 20" aria-hidden="true"><circle cx="10" cy="10" r="3.5" fill="none" stroke="var(--cocoa)" stroke-width="2"/><path d="M13.5 7 V12 C13.5 14 17 14 17 10 A7 7 0 1 0 13 16.3" fill="none" stroke="var(--cocoa)" stroke-width="2"/></svg>
        <span>Percy.Lantern@dribblecakebites.com.au</span>
      </li>
      <li>
        <svg viewBox="0 0 20 20" aria-hidden="true"><circle cx="10" cy="10" r="8" fill="none" stroke="var(--cocoa)" stroke-width="1.6"/><ellipse cx="10" cy="10" rx="3.5" ry="8" fill="none" stroke="var(--cocoa)" stroke-width="1.4"/><path d="M2 10 H18 M3.5 6 H16.5 M3.5 14 H16.5" stroke="var(--cocoa)" stroke-width="1.2"/></svg>
        <span>www.dribblecakebites.com.au</span>
      </li>
    </ul>
  </main>
</body>
</html>
```